Project Planning & Communication Process

Need a PowerPoint slide that illustrates our project planning and communication cycle. Our company has key meetings, and key communication vehicles (like emails and follow up tools) that we use to ensure our frontline staff are prepared to execute the new project successfully. This document needs to call out how the different components, like the meetings and emails, work together (like a flow chart), so someone who needs to use this process will understand what they should do. The slide needs to be simple yet comprehensive enough to guide someone through the details. I don't want it overwhelming. The primary focus is the process, not the details.

Use the color pallette included within the slide (shades of blue and gray, and black). This is for an insurance company (www.harborquill.com). Use this as a reference for the look and feel.

I have attached a sample slide of the flow chart process.

Click here if you cannot access the file. https://www.filecrate.example/s/q8wz2mbt7ypnc4r/Communcation_Methods_V1.pptx

If you are not able to see the uploaded slide.  Please send me your email address and I will send the slide to you directly. 

ISince I'm not able to upload the reference ppt file, 've uploaded the slide at FileCrate.  Please click here to access.
https://www.filecrate.example/s/q8wz2mbt7ypnc4r/Communcation_Methods_V1.pptx

Reason: extending one more day for designers to make last minute updates.

Target Market(s)

Vice Presidents and project managers/business partners within the organization.

Industry/Entity Type

Communication

Font styles to use
Sans Serif

Colors
3176b5

Requirements
Must have
• 1 page, color pallette assigned, be simple yet comprehensive. the focus needs to be on the process, not on the details.
Nice to have
• Doesn't have to follow the example I provided. Please feel free to approach from different ways.

```html
<!DOCTYPE html>
<html lang="en">
<head>
<meta charset="utf-8">
<title>Project Alignment &amp; Communication Process</title>
<link href="https://fonts.googleapis.com/css2?family=Lato:wght@300;400;700&display=swap" rel="stylesheet">
<style>
:root{
  --white:#ffffff;
  --title-blue:#4cc2ee;
  --brand-blue:#1a6fb5;
  --plan-head:#5a7cc4;
  --prep-head:#2a8fbd;
  --follow-head:#0aaef0;
  --plan-body:#e6e6e6;
  --prep-body:#c4c4c4;
  --follow-body:#7b7b7b;
  --banner:#44c4f0;
  --icon-plan:#1aa9e8;
  --icon-prep:#2a8fbd;
  --text:#5a5a5a;
  --muted:#7a7a7a;
  --note:#f0533f;
}
*{margin:0;padding:0;box-sizing:border-box}
html,body{width:1200px;height:901px;overflow:hidden;background:var(--white)}
body{font-family:"Lato",Arial,sans-serif;color:var(--text)}
.slide{position:relative;width:1200px;height:901px}
.header{position:absolute;left:0;top:0;width:1200px;height:132px;background:var(--white)}
.slide-title{position:absolute;left:52px;top:46px;font-size:30px;font-weight:300;color:var(--title-blue);letter-spacing:.2px}
.divider{position:absolute;left:734px;top:37px;width:2px;height:65px;background:var(--title-blue)}
.brand{position:absolute;left:818px;top:40px;display:flex;align-items:center;gap:14px}
.brand-name{font-size:34px;font-weight:700;color:var(--brand-blue)}
.brand-mark{width:30px;height:30px;background:var(--brand-blue)}
.column{position:absolute;top:132px;height:769px}
.col-plan{left:0;width:396px;background:var(--plan-body)}
.col-prep{left:396px;width:402px;background:var(--prep-body)}
.col-follow{left:798px;width:402px;background:var(--follow-body)}
.phase-head{height:78px;display:flex;align-items:center;justify-content:center;color:var(--white);font-size:25px;font-weight:400}
.col-plan .phase-head{background:var(--plan-head)}
.col-prep .phase-head{background:var(--prep-head)}
.col-follow .phase-head{background:var(--follow-head)}
.banner{position:absolute;height:50px;background:var(--banner);color:var(--white);font-weight:700;font-size:20px;display:flex;align-items:center;justify-content:center}
.icon{position:absolute;width:56px;height:56px;border-radius:50%;display:flex;align-items:center;justify-content:center}
.col-plan .icon{background:var(--icon-plan)}
.col-prep .icon,.col-follow .icon{background:var(--icon-prep)}
.step{position:absolute}
.step-title{font-size:22px;font-weight:300;line-height:26px;color:var(--text)}
.col-follow .step-title{color:var(--white)}
.purpose-label{font-size:16px;font-weight:700;color:var(--muted);line-height:20px;margin-top:2px}
.purpose-text{font-size:16px;font-weight:400;color:var(--muted);line-height:19px}
.note{color:var(--note)}
</style>
</head>
<body>
<div class="slide">
  <header class="header">
    <h1 class="slide-title">Project Alignment &amp; Communication Process</h1>
    <div class="divider"></div>
    <div class="brand"><span class="brand-name">Harbor Quill</span><span class="brand-mark"></span></div>
  </header>

  <section class="column col-plan">
    <div class="phase-head">Planning &amp; Design Phase</div>
    <div class="icon" style="left:38px;top:110px">
      <svg width="30" height="32" viewBox="0 0 30 32" fill="none" stroke="#fff" stroke-width="2"><path d="M15 5a8 8 0 0 0-5 14v4h10v-4a8 8 0 0 0-5-14z" fill="#fff"/><path d="M11 26h8M12 29h6M15 0v2M3 9H1M29 9h-2M6 2l1.5 1.5M24 2l-1.5 1.5"/></svg>
    </div>
    <div class="step" style="left:129px;top:104px"><div class="step-title">New Project Identified</div></div>

    <div class="banner" style="left:39px;top:186px;width:300px">3+ Months out</div>

    <div class="icon" style="left:38px;top:266px"><svg width="34" height="22" viewBox="0 0 34 22" fill="#fff"><circle cx="17" cy="5" r="4"/><circle cx="7" cy="7" r="3.3"/><circle cx="27" cy="7" r="3.3"/><path d="M10 21a7 7 0 0 1 14 0z"/><path d="M1 21a6 6 0 0 1 10-4.5A8 8 0 0 0 9 21zM33 21a6 6 0 0 0-10-4.5A8 8 0 0 1 25 21z"/></svg></div>
    <div class="step" style="left:120px;top:266px">
      <div class="step-title">Governance Meeting</div>
      <div class="purpose-label">Purpose:</div>
      <div class="purpose-text">Go/No Go Decision</div>
    </div>

    <div class="icon" style="left:38px;top:389px"><svg width="34" height="22" viewBox="0 0 34 22" fill="#fff"><circle cx="17" cy="5" r="4"/><circle cx="7" cy="7" r="3.3"/><circle cx="27" cy="7" r="3.3"/><path d="M10 21a7 7 0 0 1 14 0z"/><path d="M1 21a6 6 0 0 1 10-4.5A8 8 0 0 0 9 21zM33 21a6 6 0 0 0-10-4.5A8 8 0 0 1 25 21z"/></svg></div>
    <div class="step" style="left:120px;top:388px">
      <div class="step-title">Governance Meeting</div>
      <div class="purpose-label">Purpose:</div>
      <div class="purpose-text">Milestone status and Key<br>Decisions Points</div>
    </div>

    <div class="banner" style="left:39px;top:498px;width:300px">2 Months out</div>

    <div class="icon" style="left:38px;top:581px"><svg width="34" height="22" viewBox="0 0 34 22" fill="#fff"><circle cx="17" cy="5" r="4"/><circle cx="7" cy="7" r="3.3"/><circle cx="27" cy="7" r="3.3"/><path d="M10 21a7 7 0 0 1 14 0z"/><path d="M1 21a6 6 0 0 1 10-4.5A8 8 0 0 0 9 21zM33 21a6 6 0 0 0-10-4.5A8 8 0 0 1 25 21z"/></svg></div>
    <div class="step" style="left:120px;top:580px">
      <div class="step-title">Weekly Center<br>Leader Meeting</div>
      <div class="purpose-label">Purpose:</div>
      <div class="purpose-text">Present Project <span class="note">NOTE 1</span></div>
    </div>
  </section>

  <section class="column col-prep">
    <div class="phase-head">Prepare Phase</div>
    <div class="banner" style="left:33px;top:111px;width:318px">1+ Month out</div>

    <div class="icon" style="left:33px;top:188px"><svg width="34" height="22" viewBox="0 0 34 22" fill="#fff"><circle cx="17" cy="5" r="4"/><circle cx="7" cy="7" r="3.3"/><circle cx="27" cy="7" r="3.3"/><path d="M10 21a7 7 0 0 1 14 0z"/><path d="M1 21a6 6 0 0 1 10-4.5A8 8 0 0 0 9 21zM33 21a6 6 0 0 0-10-4.5A8 8 0 0 1 25 21z"/></svg></div>
    <div class="step" style="left:112px;top:188px">
      <div class="step-title">Weekly Center<br>Leader Meeting</div>
      <div class="purpose-label">Purpose:</div>
      <div class="purpose-text">Provide Implementation Details</div>
    </div>

    <div class="banner" style="left:33px;top:306px;width:318px">1 Week out</div>

    <div class="icon" style="left:33px;top:390px"><svg width="22" height="28" viewBox="0 0 22 28" fill="#fff"><path d="M0 0h15l7 7v21H0z"/><path d="M15 0v7h7" fill="#2a8fbd"/></svg></div>
    <div class="step" style="left:112px;top:387px">
      <div class="step-title">Monday Memo</div>
      <div class="purpose-label">Purpose:</div>
      <div class="purpose-text note">NOTE 2</div>
    </div>

    <div class="banner" style="left:33px;top:498px;width:318px">As needed</div>

    <div class="icon" style="left:33px;top:581px"><svg width="26" height="26" viewBox="0 0 26 26"><rect width="26" height="26" rx="2" fill="#fff"/><rect width="26" height="7" fill="#1e6f96"/><text x="13" y="21" text-anchor="middle" font-family="Lato,Arial,sans-serif" font-size="11" font-weight="700" fill="#2a8fbd">01</text></svg></div>
    <div class="step" style="left:112px;top:580px">
      <div class="step-title">Daily Digest</div>
      <div class="purpose-label">Purpose:</div>
      <div class="purpose-text">Provide just in time updates</div>
    </div>
  </section>

  <section class="column col-follow">
    <div class="phase-head">Follow up &amp; Evaluate</div>
    <div class="banner" style="left:40px;top:111px;width:320px">Post Launch</div>
    <div class="icon" style="left:41px;top:194px"><svg width="26" height="26" viewBox="0 0 26 26" fill="none"><rect x="2" y="3" width="20" height="20" rx="2" fill="#fff"/><path d="M7 12l5 5 12-13" stroke="#2a8fbd" stroke-width="3"/></svg></div>
    <div class="step" style="left:129px;top:190px"><div class="step-title">Follow-up Guide</div></div>
  </section>
</div>
</body>
</html>
```